Copper Lantern needs Stationary and Business Cards
Designs needs
Traditional
Delia R. Stroup
Owner
482 W. Hollin Creek Rd.
Harlow Falls, MI 49012
stroupd@lantern482.com
www.lantern482.com
What colors would you like? Black and Burnt Red
The Tavern will have an industrial chic style (updated vintage). I have attached a few clipart elements

```html
<!DOCTYPE html>
<html lang="en">
<head>
<meta charset="utf-8">
<title>Copper Lantern Business Card</title>
<link rel="stylesheet" href="https://fonts.googleapis.com/css2?family=Tinos:wght@400;700&display=swap">
<style>
  :root {
    --backdrop: #5b4036;
    --card: #ffffff;
    --ink: #1a1a1a;
    --burnt-red: #7a2a1c;
    --engraving-light: #dcdcdc;
    --engraving-dark: #5c5c5c;
  }
  * { margin: 0; padding: 0; box-sizing: border-box; }
  html, body {
    width: 1200px;
    height: 802px;
    overflow: hidden;
    background: var(--backdrop);
  }
  .canvas {
    position: relative;
    width: 1200px;
    height: 802px;
  }
  .business-card {
    position: absolute;
    left: 260px;
    top: 205px;
    width: 680px;
    height: 392px;
    background: var(--card);
    border-radius: 22px;
    overflow: hidden;
    font-family: "Tinos", "Times New Roman", serif;
    color: var(--ink);
  }
  .brand {
    position: absolute;
    left: 76px;
    top: 25px;
    width: 197px;
    height: 173px;
    display: flex;
    flex-direction: column;
    justify-content: center;
    align-items: center;
    gap: 12px;
  }
  .brand-mark {
    width: 20px;
    height: 20px;
    background: var(--burnt-red);
  }
  .brand-name {
    font-weight: 700;
    font-size: 34px;
    line-height: 1.05;
    text-align: center;
    color: var(--ink);
    letter-spacing: 1px;
  }
  .pointing-hand {
    position: absolute;
    background: linear-gradient(180deg, var(--engraving-light), var(--engraving-dark));
  }
  .pointing-hand--right-top {
    left: 406px;
    top: 29px;
    width: 274px;
    height: 146px;
    border-radius: 60px 0 0 60px;
  }
  .pointing-hand--left-bottom {
    left: 0;
    top: 235px;
    width: 269px;
    height: 148px;
    border-radius: 0 60px 60px 0;
  }
  .contact {
    position: absolute;
    left: 355px;
    top: 190px;
  }
  .contact-name {
    font-weight: 700;
    font-size: 22px;
    line-height: 26px;
  }
  .contact-role {
    font-size: 15px;
    line-height: 20px;
    margin-top: 4px;
  }
  .contact-details {
    list-style: none;
    margin-top: 26px;
    font-size: 13.5px;
    line-height: 22px;
  }
  .contact-details .label {
    font-weight: 700;
  }
</style>
</head>
<body>
<main class="canvas">
  <article class="business-card">
    <div class="brand">
      <span class="brand-mark"></span>
      <span class="brand-name">Copper<br>Lantern</span>
    </div>

    <div class="pointing-hand pointing-hand--right-top" role="img" aria-label="Vintage engraved hand pointing left"></div>
    <div class="pointing-hand pointing-hand--left-bottom" role="img" aria-label="Vintage engraved hand pointing right"></div>

    <section class="contact">
      <h1 class="contact-name">Delia R. Stroup</h1>
      <p class="contact-role">Owner</p>
      <ul class="contact-details">
        <li>482 W. Hollin Creek Rd.</li>
        <li>Harlow Falls, MI 49012</li>
        <li><span class="label">P :</span> 517.555.0148</li>
        <li><span class="label">E :</span> stroupd@lantern482.com</li>
        <li><span class="label">W :</span> www.lantern482.com</li>
      </ul>
    </section>
  </article>
</main>
</body>
</html>
```